Business Card Re-Design for a Lighting Designer

I would like my business card re-designed. It is currently high gloss and they scratch too easily. I don not think the current design lends itself well to a matte finish. I have included the current design for reference along with our company logo.
Check out our website for current branding.
http://www.brambleorchidstudio.example

Updates
Some of the top contenders are muslim and it is a holiday for them. I do not want to discriminate and would expect the same courtesy for holidays we celebrate.
Target Market(s)
Interior Designers, Architects
Contact Information for Business Card
Logo - Name, Title, Address, Telephone Number and Extension, Email
Font styles to use
Requirements
Must have
- All the information listed on the current business card. If you use Red, it needs to be the red from our logo.
Nice to have
- Vertical and Horizontal Designs will be entertained.
Should not have
- Requirements for a glossy finish...should not look too corporate since we are a design firm.

```html
<!DOCTYPE html>
<html lang="en">
<head>
<meta charset="utf-8">
<title>Bramble Orchid Studio – Business Card</title>
<link rel="stylesheet" href="https://fonts.googleapis.com/css2?family=Lato:wght@300;400;700&family=Oswald:wght@500&display=swap">
<style>
  :root {
    --brand-red: #9b0000;
    --rule-red: #c0392b;
    --ink: #2b2b2b;
    --muted: #8a8a8a;
    --paper: #ffffff;
    --backdrop: #333333;
  }
  * { box-sizing: border-box; margin: 0; padding: 0; }
  html, body { width: 1200px; height: 866px; overflow: hidden; }
  body {
    background: var(--backdrop);
    display: flex;
    align-items: center;
    justify-content: center;
    gap: 40px;
    font-family: "Lato", sans-serif;
  }
  .card {
    width: 540px;
    height: 309px;
    position: relative;
    box-shadow: 0 10px 24px rgba(0,0,0,.45);
  }
  .card--front { background: var(--paper); color: var(--ink); }
  .card--back {
    background: var(--brand-red);
    display: flex;
    align-items: center;
    justify-content: center;
  }

  .person { position: absolute; left: 34px; top: 34px; }
  .person__name {
    font-family: "Oswald", sans-serif;
    font-weight: 500;
    font-size: 26px;
    letter-spacing: .5px;
    text-transform: uppercase;
    color: var(--brand-red);
    line-height: 1;
  }
  .person__title { font-size: 14px; color: #555; margin-top: 3px; }

  .divider {
    position: absolute;
    left: 34px; right: 34px; top: 110px;
    height: 1px;
    background: var(--rule-red);
    opacity: .8;
  }

  .contact {
    position: absolute; left: 34px; top: 128px;
    list-style: none;
    font-size: 13.5px;
    line-height: 1.65;
  }
  .contact li { display: flex; align-items: center; gap: 8px; }
  .contact svg { width: 13px; height: 13px; fill: var(--brand-red); flex: none; }

  .wordmark {
    display: flex;
    align-items: center;
    gap: 10px;
    font-family: "Lato", sans-serif;
    font-weight: 400;
    text-transform: uppercase;
    letter-spacing: 1px;
    line-height: 1.05;
  }
  .wordmark__square { width: 22px; height: 22px; flex: none; }
  .wordmark__name { font-size: 20px; }
  .tagline {
    font-size: 8.5px;
    letter-spacing: 1.6px;
    text-transform: uppercase;
    margin-top: 6px;
  }

  .card--front .brand { position: absolute; right: 34px; top: 132px; text-align: left; }
  .card--front .wordmark__name { color: var(--ink); }
  .card--front .wordmark__square { background: var(--brand-red); }
  .card--front .tagline { color: var(--muted); padding-left: 32px; }

  .address {
    position: absolute; right: 34px; bottom: 26px;
    font-style: normal;
    text-align: right;
    font-size: 13.5px;
    line-height: 1.35;
  }

  .card--back .wordmark__name { color: var(--paper); font-size: 28px; }
  .card--back .wordmark__square { background: var(--paper); width: 30px; height: 30px; }
  .card--back .tagline { color: var(--paper); padding-left: 40px; font-size: 10px; }
</style>
</head>
<body>

<article class="card card--front">
  <header class="person">
    <h1 class="person__name">Marlowe Dunstan</h1>
    <p class="person__title">Principal</p>
  </header>
  <div class="divider"></div>

  <ul class="contact">
    <li>
      <svg viewBox="0 0 16 16" aria-hidden="true"><path d="M3 1l3 3-1.6 2a9 9 0 0 0 5.6 5.6L12 10l3 3-2 2C6.5 14.5 1.5 9.5 1 3z"/></svg>
      555.014.2280 x1
    </li>
    <li>
      <svg viewBox="0 0 16 16" aria-hidden="true"><path d="M1 3h14v10H1z M2 4l6 5 6-5" stroke="#fff" stroke-width="1.2"/></svg>
      marlowe@brambleorchidstudio.example
    </li>
    <li>
      <svg viewBox="0 0 16 16" aria-hidden="true"><circle cx="8" cy="8" r="7"/><path d="M1 8h14M8 1c-3 3-3 11 0 14M8 1c3 3 3 11 0 14" stroke="#fff" stroke-width="1" fill="none"/></svg>
      www.brambleorchidstudio.example
    </li>
  </ul>

  <div class="brand">
    <div class="wordmark">
      <span class="wordmark__square"></span>
      <span class="wordmark__name">Bramble<br>Orchid Studio</span>
    </div>
    <p class="tagline">Lighting for Architecture</p>
  </div>

  <address class="address">
    218 Larkspur Row<br>
    Suite 40 Fernvale<br>
    Georgia 30999 USA
  </address>
</article>

<article class="card card--back">
  <div class="brand">
    <div class="wordmark">
      <span class="wordmark__square"></span>
      <span class="wordmark__name">Bramble<br>Orchid Studio</span>
    </div>
    <p class="tagline">Lighting for Architecture</p>
  </div>
</article>

</body>
</html>
```